Green Logistics / Last Mile Delivery Firm needs cool one-page website

FYI - We do have a detailed brief in the uploaded files section below
COMPANY
We recently launched the company Brook Logistics which is a pioneer in urban green logistics and provides zero-emissions last mile delivery services (i.e. delivery of parcels with delivery vans to the doorstep of households) for its logistics and retail clients.
We take on urban parcel delivery for our clients with a 100% electric commercial vehicles fleet, fair and sustainable working conditions for our employees and an unparalleled professional and customer-focused mindset.
WEBSITE
In the detailed brief, we have provided examples to emulate. We need the design + coding of the website. Website needs to be friendly/optimized for and should open swiftly on both Android & iOS.
In general, the website should convey
- green mission of the company
- sustainability (good working conditions, focus on employees)
- customer orientation
- professionalism
DESIGN
In the detailed brief, we have provided designs to emulate.
Color design: we do have a logo which features 2 green colors (one lighter and one darker color tone). However, the colors on the website do not necessarily need to follow these 2 colors exactly as we are able to switch the logo colors.
Imagery: should reflect maybe 50% green/leaf/tree , 25% customer and employee orientation, and 25% logistics (here it's important that it is the last mile delivery, i.e. delivery with delivery vans to the doorstep of households)
Coding

```html
<!DOCTYPE html>
<html lang="en">
<head>
<meta charset="utf-8">
<title>Brook Logistics – Sustainable Last Mile</title>
<link href="https://fonts.googleapis.com/css2?family=Nunito+Sans:wght@400;700;800;900&family=Raleway:wght@400;500;600;700&display=swap" rel="stylesheet">
<style>
:root{
  --green:#1e9a3f;
  --green-deep:#137a30;
  --lime:#9cc83b;
  --lime-btn:#8cc63f;
  --ink:#1d1d1d;
  --text:#5a5a5a;
  --muted:#8a8a8a;
  --line:#e3e3e3;
  --dark:#0d1a0f;
  --white:#ffffff;
}
*{box-sizing:border-box;margin:0;padding:0}
html,body{width:1200px;height:4482px;overflow:hidden}
body{font-family:"Raleway",sans-serif;color:var(--text);background:var(--white);position:relative}
h1,h2,h3{font-family:"Nunito Sans",sans-serif;color:var(--ink)}
.btn{display:inline-block;background:var(--lime-btn);color:var(--white);font-family:"Raleway",sans-serif;font-weight:600;font-size:12px;letter-spacing:.5px;border-radius:20px;padding:10px 24px;text-transform:uppercase}
.brand{display:flex;align-items:center;gap:10px;font-family:"Nunito Sans",sans-serif;font-weight:800;color:var(--lime);text-transform:uppercase}
.brand-dot{width:36px;height:36px;border-radius:50%;background:var(--green)}

/* hero */
.hero{position:absolute;left:0;top:0;width:1200px;height:600px;background:radial-gradient(ellipse at 50% 45%,#1a2a14 0%,#0b150b 45%,#1f3a12 80%,#3e6a1c 100%)}
.nav{position:absolute;top:18px;left:92px;right:92px;display:flex;align-items:center}
.nav .brand{font-size:15px}
.nav ul{list-style:none;display:flex;margin-left:140px}
.nav li{font-size:12px;color:var(--white);width:85px}
.nav li.active{color:var(--lime)}
.nav .phone{margin-left:auto;color:var(--white);font-size:13px;line-height:1.2}
.nav .phone small{display:block;font-size:9px;color:#cfcfcf}
.nav .lang{margin-left:44px;font-size:10px;color:var(--white)}
.hero-title{position:absolute;top:232px;width:100%;text-align:center}
.hero-title h1{color:var(--white);font-size:41px;font-weight:900;letter-spacing:.5px}
.hero-title p{color:var(--white);font-size:18px;margin-top:4px}
.hero-title .btn{margin-top:16px;font-size:11px;padding:10px 22px}
.divider-mark{position:absolute;left:576px;top:578px;width:48px;height:48px;border-radius:50%;background:var(--green)}
.divider-dots{position:absolute;left:584px;top:566px;width:36px;height:4px;background:repeating-linear-gradient(90deg,#fff 0 4px,transparent 4px 7px)}

/* about */
.about-title{position:absolute;top:648px;width:100%;text-align:center;font-size:38px;font-weight:900}
.about-cards{position:absolute;top:703px;left:94px;width:1012px;height:380px;display:flex;background:var(--white);border:1px solid var(--line);z-index:2}
.about-card{flex:1;padding:22px;border-right:1px solid var(--line);position:relative}
.about-card:last-child{border-right:none}
.about-card h3{font-family:"Raleway",sans-serif;font-weight:500;font-size:18px;color:#333;margin-bottom:12px}
.about-card p{font-size:10px;line-height:1.55;color:var(--muted);margin-bottom:8px}
.about-card .narrow{width:158px}
.about-art{position:absolute;right:14px;bottom:26px;width:130px;height:140px;border-radius:6px;background:linear-gradient(135deg,#eef3f8,#dfe9d6)}

/* is band */
.is-band{position:absolute;top:1058px;left:0;width:1200px;height:487px;background:linear-gradient(180deg,#2b3d44 0%,#23392f 55%,#1c3416 100%)}
.is-band h2{position:absolute;top:110px;left:94px;color:var(--white);font-size:38px;font-weight:800}
.is-band .sub{position:absolute;top:172px;left:94px;color:var(--white);font-size:17px}
.bars{position:absolute;top:213px;left:94px}
.bar{height:33px;margin-bottom:16px;color:var(--white);font-size:13px;padding-left:11px;line-height:33px}
.bar.dark{background:var(--green)}
.bar.light{background:var(--lime)}

/* services */
.services{position:absolute;top:1545px;left:0;width:1200px;height:486px}
.svc-grid{position:absolute;top:70px;left:94px;display:grid;grid-template-columns:252px 252px;row-gap:40px}
.svc svg{width:70px;height:70px;display:block}
.svc h3{font-family:"Raleway",sans-serif;font-weight:600;font-size:16px;margin:14px 0 6px;color:#222}
.svc p{font-size:11px;line-height:1.6;color:var(--muted);width:220px}
.svc-intro{position:absolute;top:138px;left:716px;width:392px}
.svc-intro .mark{width:48px;height:48px;border-radius:50%;background:var(--green);margin-bottom:4px}
.svc-intro h2{font-size:40px;font-weight:800;margin-bottom:14px}
.svc-intro p{font-size:12px;line-height:1.75;color:var(--muted)}
.leaf-deco{position:absolute;background:radial-gradient(ellipse at 40% 40%,#5aa52a,#1e5f16 70%,transparent 71%)}

/* touch */
.touch{position:absolute;top:2031px;left:0;width:1200px;height:369px;background:radial-gradient(ellipse at 70% 30%,#233a1e,#0a140a 65%,#050a05)}
.touch .mark{position:absolute;top:80px;left:94px;width:48px;height:48px;border-radius:50%;background:var(--green)}
.touch .kicker{position:absolute;top:146px;left:94px;color:var(--white);font-size:19px}
.touch h2{position:absolute;top:168px;left:94px;color:var(--white);font-size:38px;font-weight:800}
.touch p{position:absolute;top:228px;left:94px;width:580px;color:var(--white);font-size:12px;line-height:1.75}
.touch .btn{position:absolute;top:166px;left:982px;font-size:11px;padding:11px 24px}

/* careers */
.careers{position:absolute;top:2490px;left:94px;width:1012px}
.careers h2{font-size:40px;font-weight:800;margin-bottom:16px}
.careers p{font-size:12px;line-height:1.75;color:var(--muted);margin-bottom:8px}
.accordions{position:absolute;top:2783px;left:94px;width:1012px;display:grid;grid-template-columns:484px 484px;column-gap:44px}
.acc{background:var(--green);color:var(--white);height:47px;padding:0 14px;display:flex;align-items:center;justify-content:space-between;font-size:16px;margin-bottom:17px}
.acc-note{font-size:10.5px;color:var(--muted);line-height:1.5;margin:-6px 0 12px}

/* contact */
.contact{position:absolute;top:2990px;left:94px;width:1012px}
.contact h2{font-size:40px;font-weight:800}
.contact .lead{font-size:18px;color:#333;margin:14px 0 10px}
.contact p{font-size:12px;color:var(--muted);line-height:1.7;width:920px}
.map{position:absolute;top:3151px;left:0;width:1200px;height:402px;background:linear-gradient(120deg,#e8e4dc 0%,#efece5 40%,#e2e8e0 70%,#ede9e0 100%)}
.info{position:absolute;top:3606px;left:94px}
.info-item{display:flex;gap:8px;margin-bottom:46px}
.info-item svg{width:16px;height:16px;margin-top:3px;flex:none}
.info-item h4{font-family:"Raleway",sans-serif;font-weight:500;font-size:17px;color:#333}
.info-item span{font-size:12px;color:var(--muted)}
.form{position:absolute;top:3615px;left:525px;width:581px}
.row{display:flex;gap:8px;margin-bottom:8px}
.field{flex:1;height:38px;border:1px solid #cfcfcf;font-size:10px;color:var(--muted);padding:12px}
.field.tall{height:137px}
.form .btn{display:block;width:128px;margin:16px auto 0 232px;text-align:center;padding:10px 0;font-size:11px}

/* footer */
.footer{position:absolute;top:3895px;left:0;width:1200px;height:587px;background:linear-gradient(180deg,#ffffff 0%,#dcebc9 22%,#6aa33a 45%,#1f4a14 62%,#0c1a0a 100%)}
.footer-inner{position:absolute;top:396px;left:94px;right:94px;display:flex}
.footer .brand{font-size:22px;margin-top:14px}
.footer .brand .brand-dot{width:52px;height:52px}
.copy{font-size:11px;color:var(--white);margin-top:16px}
.fcol{color:var(--white)}
.fcol h5{font-family:"Raleway",sans-serif;font-weight:500;font-size:16px;margin-bottom:14px}
.fcol li{list-style:none;font-size:10.5px;margin-bottom:10px}
.fcol p{font-size:10px;line-height:1.55}
.social li{display:flex;align-items:center;gap:8px;margin-bottom:8px}
.social i{width:24px;height:24px;border-radius:50%;background:var(--white);display:block}
</style>
</head>
<body>

<section class="hero" role="img" aria-label="Dark close-up photo of green leaves framing the hero">
  <nav class="nav">
    <div class="brand"><span class="brand-dot"></span>Brook Logistics</div>
    <ul>
      <li class="active">Home</li><li>About</li><li>Services</li><li>Careers</li><li>Contact</li>
    </ul>
    <div class="phone">+1 (555) 014 2277<small>info@brooklogistics.com</small></div>
    <div class="lang">En ▾</div>
  </nav>
  <div class="hero-title">
    <h1>BROOK LOGISTICS – SUSTAINABLE LAST MILE</h1>
    <p>Because we care about trees!</p>
    <span class="btn">Get started</span>
  </div>
</section>
<div class="divider-dots"></div>
<div class="divider-mark"></div>

<h2 class="about-title">ABOUT US</h2>
<div class="about-cards">
  <article class="about-card">
    <h3>Who We Are</h3>
    <p>Brook Logistics is a pioneer in urban green logistics and provides zero-emissions last mile delivery services for its logistics and retail clients.</p>
    <p class="narrow">We take on urban parcel delivery for our clients with a 100% electric commercial vehicles fleet, fair and sustainable working conditions for our employees and an unparalleled professional and customer-focused mindset.</p>
    <div class="about-art" role="img" aria-label="Illustration of a team working together"></div>
  </article>
  <article class="about-card">
    <h3>Our Mission</h3>
    <p>To satisfy consumers' ever-rising desire to buy products online, the CO2 emissions from delivery traffic will increase by 32% in the top 100 cities globally until 2030.</p>
    <p class="narrow">Our clients care about our planet the same way we do, which is why Brook Logistics helps to make the planet a better place by running the most environmentally friendly urban last mile possible.</p>
    <div class="about-art" role="img" aria-label="Illustration of a delivery van and parcels tracked on a phone"></div>
  </article>
  <article class="about-card">
    <h3>Our Value</h3>
    <p>We see ourselves as a professional services company who strongly cares about the environment, its clients and their customers, as well as its employees.</p>
    <p class="narrow">We believe that delivering parcels with zero emissions and providing a unique customer experience through a highly professional attitude and a great team spirit are the cornerstones for Brook Logistics to operate in today's world in a sustainable yet profitable way.</p>
    <div class="about-art" role="img" aria-label="Illustration of a green tree with roots"></div>
  </article>
</div>

<section class="is-band" role="img" aria-label="Photo of a green field under a dusky sky">
  <h2>BROOK LOGISTICS IS...</h2>
  <div class="sub">A pioneering Green Last Mile</div>
  <div class="bars">
    <div class="bar dark" style="width:1012px">Delivering parcels emissions-free</div>
    <div class="bar light" style="width:810px">Putting customer experience first</div>
    <div class="bar dark" style="width:915px">Operating the business sustainably</div>
    <div class="bar light" style="width:876px">Focusing on the environment, customers and employees</div>
    <div class="bar dark" style="width:743px">A professional services company</div>
  </div>
</section>

<section class="services">
  <div class="leaf-deco" style="right:0;top:0;width:150px;height:200px" role="img" aria-label="Decorative monstera leaves"></div>
  <div class="svc-grid">
    <div class="svc">
      <svg viewBox="0 0 70 70"><rect x="6" y="22" width="40" height="28" fill="none" stroke="#1f3a4d" stroke-width="3"/><path d="M46 30h10l8 10v10H46z" fill="none" stroke="#1f3a4d" stroke-width="3"/><circle cx="18" cy="54" r="5" fill="#1f3a4d"/><circle cx="54" cy="54" r="5" fill="#1f3a4d"/><path d="M24 28l-6 10h8l-4 8" fill="none" stroke="#1e9a3f" stroke-width="3"/></svg>
      <h3>Zero-Emission Delivery</h3>
      <p>We operate a 100% electric commercial vehicle fleet</p>
    </div>
    <div class="svc">
      <svg viewBox="0 0 70 70"><rect x="24" y="14" width="22" height="36" rx="4" fill="none" stroke="#1f3a4d" stroke-width="3"/><line x1="24" y1="32" x2="46" y2="32" stroke="#1f3a4d" stroke-width="3"/><line x1="26" y1="58" x2="44" y2="58" stroke="#1f3a4d" stroke-width="3"/><line x1="30" y1="50" x2="27" y2="58" stroke="#1f3a4d" stroke-width="3"/><line x1="40" y1="50" x2="43" y2="58" stroke="#1f3a4d" stroke-width="3"/></svg>
      <h3>Highly Trained Delivery Drivers</h3>
      <p>We only employ permanently, train far above average, and live a great team spirit</p>
    </div>
    <div class="svc">
      <svg viewBox="0 0 70 70"><circle cx="35" cy="35" r="22" fill="none" stroke="#1f3a4d" stroke-width="6" stroke-dasharray="7 5"/><circle cx="35" cy="35" r="14" fill="none" stroke="#1f3a4d" stroke-width="3"/><circle cx="35" cy="35" r="5" fill="#1e9a3f"/></svg>
      <h3>Professional All Around</h3>
      <p>We honor our commitments and hold ourselves to the highest professional standards</p>
    </div>
    <div class="svc">
      <svg viewBox="0 0 70 70"><circle cx="22" cy="22" r="6" fill="#1f3a4d"/><circle cx="48" cy="22" r="6" fill="#1f3a4d"/><path d="M12 44c0-8 4-12 10-12s10 4 10 12z" fill="#1f3a4d"/><path d="M38 44c0-8 4-12 10-12s10 4 10 12z" fill="#1f3a4d"/><rect x="28" y="46" width="14" height="12" fill="#1e9a3f"/></svg>
      <h3>Unparalleled Customer Focus</h3>
      <p>We live a customer-oriented mindset, always measuring ourselves against their experience</p>
    </div>
  </div>
  <div class="svc-intro">
    <div class="mark"></div>
    <h2>OUR SERVICES</h2>
    <p>Brook Logistics provides last mile delivery services in urban areas to clients in the logistics and retail space. Our permanent employees are all highly trained and commit to highest professional standards which we continuously review and further develop with them.</p>
  </div>
</section>

<section class="touch" role="img" aria-label="Dark photo of large green leaves">
  <div class="mark"></div>
  <div class="kicker">GET IN TOUCH</div>
  <h2>WITH BROOK LOGISTICS</h2>
  <p>If you got excited, or have a question about our services, our approach, our jobs or just want to get in touch to chat about how green logistics can make the planet a little bit better, please get in touch!</p>
  <span class="btn">Contact us</span>
</section>

<section class="careers">
  <h2>CAREERS</h2>
  <p>If you join Brook Logistics, you join a family. We elevate one another, care for each other's wellbeing and growth, and celebrate our successes. We strongly believe growth is a team sport and that every member of the family fully contributes to the achievements of the company overall.</p>
  <p>At the heart of everything we do at Brook Logistics is a relentless focus on our mission. That's why we aim to ensure our employees can follow their own passion at the workplace, be this working in a truly collaborative and caring team, putting a smile on a customer's face or making the world a better place.</p>
  <p>While we are helping our clients grow by delivering their parcels, we are also helping all our employees grow personally and professionally. We care about our employees' happiness and wellbeing which is why we provide additional benefits like supplementary health insurance.</p>
  <p>If you are excited about joining our Brook Logistics family, please check out our open positions.</p>
</section>
<div class="accordions">
  <div>
    <div class="acc">Full-time driver / parcel deliverer (m/f/d) for Berlin <span>-</span></div>
    <p class="acc-note">As a partner for our clients, we are looking for additional members of the Brook Logistics Family in Berlin as soon as possible.</p>
    <div class="acc">Your tasks as a delivery driver: <span>+</span></div>
  </div>
  <div>
    <div class="acc">Required knowledge and skills: <span>+</span></div>
    <div class="acc">What you can expect from the Brook Logistics family: <span>+</span></div>
  </div>
</div>

<div class="leaf-deco" style="right:0;top:2920px;width:150px;height:220px" role="img" aria-label="Decorative tropical leaves"></div>
<section class="contact">
  <h2>CONTACT</h2>
  <div class="lead">We'd love to hear from you!</div>
  <p>Whether you have a question about our services, our approach, our jobs or just want to get in touch to chat about how green logistics can make the planet a little bit better, our team is ready to answer your questions and enquiries.</p>
</section>
<div class="map" role="img" aria-label="Street map showing the office location"></div>

<div class="info">
  <div class="info-item">
    <svg viewBox="0 0 16 16"><path d="M8 1a5 5 0 0 0-5 5c0 4 5 9 5 9s5-5 5-9a5 5 0 0 0-5-5z" fill="#1e9a3f"/><circle cx="8" cy="6" r="2" fill="#fff"/></svg>
    <div><h4>Location:</h4><span>27 Fernbank Road, Greenhollow, NY 10123</span></div>
  </div>
  <div class="info-item">
    <svg viewBox="0 0 16 16"><rect x="1" y="3" width="14" height="10" fill="#1e9a3f"/><path d="M1 3l7 6 7-6" fill="none" stroke="#fff" stroke-width="1.3"/></svg>
    <div><h4>Email:</h4><span>info@brooklogistics.com</span></div>
  </div>
  <div class="info-item">
    <svg viewBox="0 0 16 16"><path d="M3 1l3 3-2 2c1 3 3 5 6 6l2-2 3 3-2 2C7 15 1 9 1 3z" fill="#1e9a3f"/></svg>
    <div><h4>Call:</h4><span>+1 (555) 014 2277</span></div>
  </div>
</div>
<form class="form">
  <div class="row"><div class="field">Name:</div><div class="field">Name:</div></div>
  <div class="row"><div class="field">Subjects:</div></div>
  <div class="row"><div class="field tall">Message:</div></div>
  <span class="btn">Send message</span>
</form>

<footer class="footer" role="img" aria-label="Photo of fresh grass blades against a dark background">
  <div class="footer-inner">
    <div style="width:285px">
      <div class="brand"><span class="brand-dot"></span>Brook Logistics</div>
      <div class="copy">© 2020 Brook Logistics. All rights reserved.</div>
    </div>
    <div class="fcol" style="width:146px">
      <h5>Quick Links</h5>
      <ul><li>Home</li><li>About Us</li><li>Services</li><li>Careers</li><li>Contact Us</li></ul>
    </div>
    <div class="fcol social" style="width:160px">
      <h5>Follow Us On</h5>
      <ul><li><i></i>Friendwall</li><li><i></i>Chirper</li><li><i></i>Workline</li></ul>
    </div>
    <div class="fcol" style="width:237px">
      <h5>Legal Notice</h5>
      <p style="width:190px">If you use this site regularly and would like to help keep the site on the internet, please consider donating a small sum.</p>
    </div>
    <div class="fcol">
      <h5>Privacy Policy</h5>
      <p style="width:190px">If you use this site regularly and would like to help keep the site on the internet, please consider donating a small sum.</p>
    </div>
  </div>
</footer>

</body>
</html>
```